Verpackungen für modernes Matcha-Set
Zielgruppe
Verkauf von modernen Matcha-Sets über Kordix & Online Shop.
Aufgabenstellung
Es handelt sich um 2 Verpackungen: 1xInnenverpackung für einen Milchaufschäumer (7x7x25,5 cm) -> Design mit Firmenlogo. 1x Geschenkbox-Verpackung (ca. 32x24x11cm - genaue Daten folgen), wo alle Bestandteile des Sets enthalten sind. Das Design der Geschenkverpackung soll modern und luxuriös sein und alle Produkt- und Herstellerkennzeichnungen enthalten. Die Hauptfarbe der Verpackung sollte grün sein. Logo, Schriftart des Logos und Farbcodes sind im Anhang, sowie Fotos der Sample Ware und KI generierte Bilder wie die Produktbilder am Ende aussehen könnten.

```html
<!DOCTYPE html>
<html lang="de">
<head>
<meta charset="utf-8">
<title>VERELLA Matcha-Set Verpackung</title>
<link href="https://fonts.googleapis.com/css2?family=Cormorant+Garamond:wght@400;500&display=swap" rel="stylesheet">
<style>
  :root {
    --green-deep: #1c3121;
    --green-pattern: #2f4a33;
    --cream: #efe6d2;
    --cream-light: #f6f0df;
    --stage: #ebe9e5;
    --ink: #2c3a2e;
  }
  * { box-sizing: border-box; margin: 0; padding: 0; }
  html, body { width: 887px; height: 1200px; overflow: hidden; }
  body {
    background: var(--stage);
    font-family: "Cormorant Garamond", Georgia, serif;
    position: relative;
  }
  .lid {
    position: absolute; left: 143px; top: 70px;
    width: 600px; height: 450px;
    background: var(--green-deep);
    display: flex;
  }
  .lid-pattern {
    width: 160px; height: 100%;
    background: linear-gradient(160deg, var(--green-pattern), #28402c);
  }
  .lid-band {
    flex: 1;
    background: var(--green-deep);
    display: flex; flex-direction: column; align-items: center;
    padding-top: 150px;
    color: var(--cream);
  }
  .brand-mark {
    width: 34px; height: 34px; border-radius: 50%;
    background: var(--cream);
    margin-bottom: 14px;
  }
  .brand-name {
    font-size: 50px; font-weight: 500; letter-spacing: 1px; line-height: 1;
  }
  .set-title {
    margin-top: 112px;
    font-size: 15px; letter-spacing: 6px; font-weight: 500;
  }
  .set-icons { display: flex; gap: 18px; margin-top: 16px; }
  .set-icons svg { width: 22px; height: 24px; }
  .side-panel {
    position: absolute; left: 143px; top: 560px;
    width: 600px; height: 170px;
    background: var(--cream);
    padding: 26px 40px;
    color: var(--ink);
  }
  .side-title { font-size: 26px; font-weight: 500; margin-bottom: 10px; }
  .side-copy { font-size: 13px; line-height: 1.45; max-width: 440px; }
  .brand-strip {
    position: absolute; left: 0; bottom: 0;
    width: 887px; height: 170px;
    background: var(--cream-light);
    display: flex; align-items: center; justify-content: center; gap: 14px;
    color: var(--green-deep);
  }
  .brand-strip .brand-mark { background: var(--green-deep); margin: 0; width: 40px; height: 40px; }
  .brand-strip .brand-name { font-size: 34px; }
</style>
</head>
<body>
  <section class="lid">
    <div class="lid-pattern" role="img" aria-label="Ornamentmuster aus Blattrosetten in Grüntönen"></div>
    <div class="lid-band">
      <div class="brand-mark"></div>
      <div class="brand-name">VERELLA</div>
      <div class="set-title">MATCHA-SET</div>
      <div class="set-icons">
        <svg viewBox="0 0 22 24" fill="none" stroke="#efe6d2" stroke-width="0.8"><rect x="0.5" y="3" width="21" height="20" rx="3"/><path d="M8 1v12h6V1M11 13v5M8 20h6"/></svg>
        <svg viewBox="0 0 22 24" fill="none" stroke="#efe6d2" stroke-width="0.8"><rect x="0.5" y="3" width="21" height="20" rx="3"/><path d="M6 7h10v12H6zM16 10h3v5h-3"/></svg>
        <svg viewBox="0 0 22 24" fill="none" stroke="#efe6d2" stroke-width="0.8"><rect x="0.5" y="3" width="21" height="20" rx="3"/><circle cx="11" cy="10" r="5"/><path d="M11 15v7"/></svg>
        <svg viewBox="0 0 22 24" fill="none" stroke="#efe6d2" stroke-width="0.8"><rect x="0.5" y="3" width="21" height="20" rx="3"/><ellipse cx="14" cy="17" rx="4" ry="3"/><path d="M11 15L4 7"/></svg>
      </div>
    </div>
    <div class="lid-pattern" role="img" aria-label="Ornamentmuster aus Blattrosetten in Grüntönen"></div>
  </section>

  <section class="side-panel">
    <h2 class="side-title">MATCHA-SET</h2>
    <p class="side-copy">Feiner Matcha aus Japan, sorgfältig gemahlen. Mit Besen, Kanne, Sieb und Löffel für die tägliche Zubereitung. Trocken lagern, vor Licht schützen. Inhalt: ein vollständiges Set für zu Hause.</p>
  </section>

  <footer class="brand-strip">
    <div class="brand-mark"></div>
    <div class="brand-name">VERELLA</div>
  </footer>
</body>
</html>
```